E-brochure to promote our franchise opportunity to potential finance professionals

We need my words putting into a brochure, setting out, adding photographs and images ready for publication as a .pdf
The brochure needs to be readable as a pdf, I have no plans to publish on paper so should be well structured for a screen or tablet - easy navigation and a positive and striking visual feel

Target Market(s)

Potential business owners in business finance arranging - existing business bankers leaving their post, mortgage brokers expanding their business or existing commercial finance brokers looking for a means to expand their reach and have the help and support of a franchisor organisation

Industry/Entity Type

Finance

Font styles to use
Serif
Script

Colors
0555a3
eaf2ce

Requirements
Must have
• The project must have a professional but still accessible feel, we are not aiming to be a "corporate" like a merchant bank, our clients are ordinary small business owners, like you, so we need to speak their language. Our business is about the people we help, the dreams that come true because we help them and the wealth we create for them.
Nice to have
• Great artwork, interesting photographs, a compelling front cover page, pages which are easily readable, not too text heavy but getting the point across
Should not have
• Should not be boring - over corporate or too frivolous

```html
<!DOCTYPE html>
<html lang="en">
<head>
<meta charset="utf-8">
<title>Larchmont Lending – Franchise Opportunity</title>
<link rel="stylesheet" href="https://fonts.googleapis.com/css2?family=Tinos:ital,wght@0,400;0,700;1,400;1,700&family=Courgette&display=swap">
<style>
:root{
  --brand-blue:#0555a3;
  --ink-navy:#1d3559;
  --cream:#eaf2ce;
  --mist:#9aa3a8;
  --body-ink:#2a2a2a;
  --stage:#8d8d8d;
  --paper:#ffffff;
}
*{box-sizing:border-box;margin:0;padding:0}
html,body{width:1200px;height:982px;overflow:hidden}
body{background:var(--stage);position:relative;font-family:"Tinos","Times New Roman",serif;color:var(--body-ink)}
.page{position:absolute;top:229px;width:374px;height:524px;background:var(--paper);overflow:hidden;box-shadow:0 4px 10px rgba(0,0,0,.35)}
.page--cover{left:15px}
.page--summary{left:412px}
.page--back{left:812px}

/* wordmark */
.wordmark{position:absolute;display:flex;align-items:center;gap:9px}
.wordmark__dot{width:24px;height:24px;border-radius:50%;background:var(--mist);flex:none}
.wordmark__name{font-size:24px;line-height:1;color:var(--ink-navy);white-space:nowrap}
.wordmark__tag{font-size:9px;color:var(--mist);margin-top:4px;white-space:nowrap}

/* cover */
.cover__rule{position:absolute;left:0;top:85px;width:100%;height:4px;background:var(--cream)}
.cover__photo{position:absolute;left:0;top:89px;width:374px;height:341px;background:linear-gradient(160deg,#c9b8a0 0%,#8d7a63 45%,#4f4a45 100%)}
.cover__base{position:absolute;left:0;top:420px;width:374px;height:104px}
.cover__title{position:absolute;left:16px;top:466px;font-size:9.5px;letter-spacing:.6px;color:#fff}
.cover__meta{position:absolute;left:16px;top:480px;font-size:6.5px;line-height:11px;color:#fff}
.cover__web{position:absolute;right:17px;top:504px;font-size:6px;letter-spacing:2px;color:#fff}

/* summary */
.tab{position:absolute;left:0;top:42px;width:146px;height:15px;background:var(--brand-blue);color:#fff;font-size:7.5px;letter-spacing:.4px;font-weight:700;padding:2px 0 0 35px}
.block{position:absolute;left:34px;width:302px}
.block__head{font-family:"Courgette",cursive;color:var(--brand-blue);font-size:8.5px;margin-bottom:5px}
.block p,.block li{font-size:6.5px;line-height:11px;text-align:justify}
.block ul{list-style:none;margin-top:5px}
.block li{position:relative;padding-left:9px}
.block li::before{content:"";position:absolute;left:0;top:4px;width:3px;height:3px;border-radius:50%;background:var(--brand-blue)}
.link{color:var(--brand-blue)}
.summary__footer{position:absolute;left:0;top:478px;width:374px;height:46px}
.summary__mark{position:absolute;right:39px;top:500px;color:#fff;font-size:8.5px;font-style:italic;letter-spacing:.6px}

/* back */
.back__photo{position:absolute;left:0;top:0;width:374px;height:260px;background:linear-gradient(180deg,#cfcfcf 0%,#dcdcdc 55%,#ffffff 100%)}
.back__base{position:absolute;left:0;top:400px;width:374px;height:124px}
.back__head{position:absolute;left:16px;top:434px;color:#fff;font-size:7px;font-weight:700;text-decoration:underline}
.back__col{position:absolute;width:162px;color:#fff;list-style:none}
.back__col li{position:relative;font-size:6.5px;line-height:11px;padding-left:9px;margin-bottom:4px;text-align:justify}
.back__col li::before{content:"";position:absolute;left:0;top:3.5px;width:3px;height:3px;border:1px solid #fff;border-radius:50%}
</style>
</head>
<body>

<section class="page page--cover">
  <div class="wordmark" style="left:80px;top:26px">
    <span class="wordmark__dot"></span>
    <div><div class="wordmark__name">Larchmont Lending</div><div class="wordmark__tag">Practical finance for growing firms</div></div>
  </div>
  <div class="cover__rule"></div>
  <div class="cover__photo" role="img" aria-label="Photo of a smiling team of five young professionals in a bright office"></div>
  <svg class="cover__base" viewBox="0 0 374 104" aria-hidden="true">
    <path d="M0 10 H51 L70 22 L89 10 H374 V104 H0Z" fill="var(--brand-blue)"/>
    <path d="M0 8 H51 L70 20 L89 8 H374" fill="none" stroke="var(--cream)" stroke-width="3"/>
  </svg>
  <div class="cover__title">FRANCHISE OPPORTUNITY</div>
  <div class="cover__meta">Prepared for:<br>Prepared by: Mark Ellison, Principal.<br>3 October 2016</div>
  <div class="cover__web">www.larchmontlending.co.uk</div>
</section>

<section class="page page--summary">
  <div class="tab">EXECUTIVE SUMMARY</div>
  <div class="block" style="top:83px">
    <div class="block__head">Objective:</div>
    <p>Now in it's 20th year <span class="link">Larchmont Lending</span> is one of the UK's leading commercial finance brokers. It is our aim to broaden our customer base and to grow into a national UK name by the opening of Larchmont Lending branches throughout the country.</p>
    <p>Small business is the lifeblood of the UK economy yet the high street banks pay lip-service to providing full support. Contrast this with the hundreds of other lenders in the market and there is a healthy level of funding available for the small business yet many are unaware of the options available to them. More than 60% of small business owners begin and end their search for finance with their own bank, <b><i>regardless of success</i></b></p>
  </div>
  <div class="block" style="top:205px">
    <div class="block__head">Goals:</div>
    <p>It is our goal to grow the broker introduced business finance sector to similar levels to those of the insurance or residential mortgage markets and to make the name <span class="link">Larchmont Lending</span> as well known as the high street banks.</p>
  </div>
  <div class="block" style="top:282px">
    <div class="block__head">Solution</div>
    <p>In order to facilitate this growth <span class="link">Larchmont Lending</span> will be available as a franchise to ambitious finance professionals,</p>
    <ul><li>existing commercial brokers looking to strengthen their product offering and market presence and to commercial bankers looking to grow their careers outside the corporate structure.</li></ul>
  </div>
  <div class="block" style="top:363px">
    <div class="block__head">Project Outline</div>
    <p>Launching a market leading franchise network of professional commercial finance brokers with nationwide coverage.</p>
    <ul><li>Regional coverage.</li><li>Local representation.</li><li>Highest levels of customer service in the industry.</li></ul>
  </div>
  <svg class="summary__footer" viewBox="0 0 374 46" aria-hidden="true">
    <path d="M0 5 H36 L43 1 L50 5 H374" fill="none" stroke="var(--brand-blue)" stroke-width="1.2"/>
    <rect x="0" y="8" width="374" height="38" fill="var(--brand-blue)"/>
  </svg>
  <div class="summary__mark">LARCHMONT LENDING</div>
</section>

<section class="page page--back">
  <div class="back__photo" role="img" aria-label="Faded photo of colleagues meeting around a table in an office"></div>
  <div class="wordmark" style="left:76px;top:326px">
    <span class="wordmark__dot"></span>
    <div><div class="wordmark__name">Larchmont Lending</div><div class="wordmark__tag">Practical finance for growing firms</div></div>
  </div>
  <svg class="back__base" viewBox="0 0 374 124" aria-hidden="true">
    <path d="M0 11 H44 L55 17 L66 11 H374 V124 H0Z" fill="var(--brand-blue)"/>
    <path d="M0 8 H44 L55 14 L66 8 H374" fill="none" stroke="var(--brand-blue)" stroke-width="1.2"/>
  </svg>
  <div class="back__head">JOINING LARCHMONT LENDING</div>
  <ul class="back__col" style="left:16px;top:449px">
    <li>With a minimum investment of only £8,500 the <b>Larchmont Lending</b> offers fantastic value for money and the opportunity to join a growing, professional business and to secure your future income.</li>
  </ul>
  <ul class="back__col" style="left:196px;top:449px">
    <li>To apply please make contact by phone in the first instance, this will then be followed up with a business plan and a full interview.</li>
    <li>Projected income £75,000 in year one, growing thereafter.</li>
  </ul>
</section>

</body>
</html>
```